Postcard Design Project A Healthy reminder

Dr.'s Desmond and Lena torvik. Internal Medicine/Family practice. This postcard will be for our patients that we have not seen in a while. Also we need another postcard (the one your designing) with a different heading for New patient's. Do you offer a price break for that? The only thing we would need to change is the heading. Please let me know. Thank you so much! Also can you use the map on the last postcard and our logo I made? I cant find it. Please feel free to call me or email me.

```html
<!DOCTYPE html>
<html lang="en">
<head>
<meta charset="utf-8">
<title>A Healthy Reminder – Postcard</title>
<link href="https://fonts.googleapis.com/css2?family=Oswald:wght@500;700&family=Lato:wght@400;700&display=swap" rel="stylesheet">
<style>
  :root{
    --red:#c8202a;
    --black:#0d0d0d;
    --white:#ffffff;
    --panel:#efefef;
    --bg:#474747;
    --photo-a:#d9cfc4;
    --photo-b:#8a7466;
    --map-a:#eef0ea;
    --map-b:#d6dccf;
  }
  *{margin:0;padding:0;box-sizing:border-box}
  html,body{width:1200px;height:1200px;overflow:hidden;background:var(--bg)}
  body{position:relative;font-family:'Lato',sans-serif;color:var(--black)}
  .card{position:absolute;background:var(--white);overflow:hidden;box-shadow:6px 8px 14px rgba(0,0,0,.45)}
  .front{left:114px;top:86px;width:728px;height:494px}
  .back{left:349px;top:614px;width:738px;height:500px}
  .photo{position:absolute;left:0;top:0;width:728px;height:300px;
    background:linear-gradient(120deg,var(--photo-a) 0%,#efe9e2 40%,var(--photo-b) 100%)}
  .front .wave{position:absolute;left:0;top:0}
  .brand{position:absolute;display:flex;flex-direction:column;align-items:center;transform:translateX(-50%)}
  .brand-row{display:flex;align-items:center;gap:6px}
  .brand-mark{width:12px;height:12px;background:var(--red)}
  .brand-name{font-family:'Lato',sans-serif;font-weight:700;font-size:13px;color:var(--black);white-space:nowrap}
  .brand-tag{font-size:7px;letter-spacing:1px;font-weight:700;margin-top:26px;white-space:nowrap}
  .front .brand{left:133px;top:342px}
  .headline{position:absolute;left:233px;top:304px;font-family:'Oswald',sans-serif;font-weight:700;
    font-size:53px;line-height:1;color:var(--red);white-space:nowrap}
  .subline{position:absolute;left:233px;top:370px;font-family:'Oswald',sans-serif;font-weight:500;
    font-size:39px;line-height:1;color:var(--black);white-space:nowrap}
  .contact-bar{position:absolute;left:0;top:422px;width:728px;height:56px;background:var(--black);color:var(--white)}
  .red-strip{position:absolute;left:0;top:478px;width:728px;height:16px;background:var(--red)}
  .ci{position:absolute;display:flex;gap:8px;align-items:flex-start;font-size:16px;line-height:19px;white-space:nowrap}
  .ci svg{flex:none;margin-top:2px}
  .ci.phone{left:28px;top:12px;font-size:19px;font-weight:700}
  .ci.addr{left:212px;top:13px}
  .ci.web{left:478px;top:10px}
  .back .shape{position:absolute;left:0;top:0}
  .mission-title{position:absolute;left:27px;top:22px;font-family:'Oswald',sans-serif;font-weight:700;font-size:35px;color:var(--red);line-height:1.1}
  .mission-copy{position:absolute;left:27px;top:72px;width:332px;font-size:12.4px;line-height:15.8px}
  .mission-copy p{margin-bottom:15.8px}
  .call-btn{position:absolute;left:27px;top:323px;width:196px;height:37px;border-radius:19px;background:var(--red);
    color:var(--white);font-size:19px;font-weight:700;display:flex;align-items:center;justify-content:center;gap:8px}
  .back .ci{color:var(--white)}
  .back .ci.addr{left:27px;top:385px;font-size:16px}
  .back .ci.web{left:27px;top:431px;font-size:16px}
  .social{position:absolute;left:31px;top:463px;color:var(--white);font-size:12.5px}
  .map{position:absolute;left:301px;top:276px;width:136px;height:136px;border-radius:50%;
    background:radial-gradient(circle at 45% 45%,var(--map-a),var(--map-b));border:5px solid var(--white);
    box-shadow:0 0 0 3px var(--red)}
  .back .brand{left:477px;top:64px}
  .stamp{position:absolute;left:630px;top:29px;width:76px;height:84px;background:#ececec}
  .addr-line{position:absolute;left:532px;width:177px;height:2px;background:var(--black)}
</style>
</head>
<body>

<section class="card front">
  <div class="photo" role="img" aria-label="Photo of two doctors in white coats reviewing a patient chart in a clinic hallway"></div>
  <svg class="wave" width="728" height="320" viewBox="0 0 728 320">
    <path d="M0 255 C220 245 420 282 560 273 C650 265 700 220 728 175 L728 320 L0 320 Z" fill="var(--black)"/>
    <path d="M0 259 C220 250 420 290 560 282 C650 274 705 232 728 208 L728 320 L0 320 Z" fill="var(--red)"/>
    <path d="M0 280 C220 268 420 298 570 289 C660 282 710 246 728 228 L728 320 L0 320 Z" fill="var(--white)"/>
  </svg>
  <div class="brand">
    <div class="brand-row"><span class="brand-mark"></span><span class="brand-name">Desmond T Torvik, M.D.</span></div>
    <div class="brand-tag">A Primary Care Office</div>
  </div>
  <h1 class="headline">A Healthy Remainder</h1>
  <p class="subline">it is time for your annual exam</p>
  <div class="contact-bar">
    <div class="ci phone">
      <svg width="16" height="16" viewBox="0 0 16 16"><circle cx="8" cy="8" r="7" fill="none" stroke="var(--red)" stroke-width="1.5"/><path d="M5.5 4.5l1.5 1.7-.8 1c.6 1 1.3 1.7 2.3 2.3l1-.8 1.7 1.5-1 1.2C8 11 5 8 4.5 5.5z" fill="var(--red)"/></svg>
      <span>(555) 014-2290</span>
    </div>
    <div class="ci addr">
      <svg width="14" height="18" viewBox="0 0 14 18"><path d="M7 0C3 0 0 3 0 7c0 5 7 11 7 11s7-6 7-11c0-4-3-7-7-7z" fill="var(--red)"/><circle cx="7" cy="7" r="2.6" fill="var(--black)"/></svg>
      <span>4280 N. Alder Street Suite 210<br>Maple Grove, Ca 93000</span>
    </div>
    <div class="ci web">
      <svg width="16" height="16" viewBox="0 0 16 16" fill="none" stroke="var(--red)" stroke-width="1.3"><circle cx="8" cy="8" r="7"/><ellipse cx="8" cy="8" rx="3" ry="7"/><path d="M1 8h14M2.5 4.5h11M2.5 11.5h11"/></svg>
      <span>www.desmondtorvikmd.com</span>
    </div>
  </div>
  <div class="red-strip"></div>
</section>

<section class="card back">
  <svg class="shape" width="738" height="500" viewBox="0 0 738 500">
    <path d="M0 0 L395 0 C395 60 380 120 400 200 C420 280 400 400 380 500 L0 500 Z" fill="var(--panel)"/>
    <path d="M0 369 L412 369 C405 420 395 460 380 500 L0 500 Z" fill="var(--black)"/>
    <path d="M395 0 C380 80 380 130 400 200 C422 280 405 400 380 500" fill="none" stroke="var(--red)" stroke-width="7"/>
  </svg>
  <h2 class="mission-title">Our Mission</h2>
  <div class="mission-copy">
    <p>Our office is committed to working with each individual patient to achieve and maintain their optimal wellbeing. We strive to deliver high quality, compassionate care. We are committed to offering affordable medical services to patients in an atmosphere of respect, professionalism and confidentiality.</p>
    <p>Our Physicians and healthcare staff are dedicated to providing thorough, informative healthcare. We promise our patients to keep them up to date, educated, and informed. We are confident our care is of the utmost quality, and the needs of our patients will always be our first priority.</p>
    <p>We look forward to working together closely<br>towards a healthier future</p>
  </div>
  <div class="call-btn">
    <svg width="16" height="16" viewBox="0 0 16 16"><circle cx="8" cy="8" r="7" fill="none" stroke="var(--white)" stroke-width="1.5"/><path d="M5.5 4.5l1.5 1.7-.8 1c.6 1 1.3 1.7 2.3 2.3l1-.8 1.7 1.5-1 1.2C8 11 5 8 4.5 5.5z" fill="var(--white)"/></svg>
    <span>(555) 014-2290</span>
  </div>
  <div class="ci addr">
    <svg width="14" height="18" viewBox="0 0 14 18"><path d="M7 0C3 0 0 3 0 7c0 5 7 11 7 11s7-6 7-11c0-4-3-7-7-7z" fill="var(--red)"/><circle cx="7" cy="7" r="2.6" fill="var(--black)"/></svg>
    <span>4280 N. Alder Street Suite 210<br>Maple Grove, Ca 93000</span>
  </div>
  <div class="ci web">
    <svg width="16" height="16" viewBox="0 0 16 16" fill="none" stroke="var(--red)" stroke-width="1.3"><circle cx="8" cy="8" r="7"/><ellipse cx="8" cy="8" rx="3" ry="7"/><path d="M1 8h14M2.5 4.5h11M2.5 11.5h11"/></svg>
    <span>www.desmondtorvikmd.com</span>
  </div>
  <div class="social">visit us on social media</div>
  <div class="map" role="img" aria-label="Street map showing the office location"></div>
  <div class="brand">
    <div class="brand-row"><span class="brand-mark"></span><span class="brand-name">Desmond T Torvik, M.D.</span></div>
    <div class="brand-tag">A Primary Care Office</div>
  </div>
  <div class="stamp"></div>
  <div class="addr-line" style="top:219px"></div>
  <div class="addr-line" style="top:254px"></div>
  <div class="addr-line" style="top:290px"></div>
</section>

</body>
</html>
```